Larkvale Residences Stationery Design Project

Simple with logo at top, address and contact information along bottom.
Hi Designers: If interested, this Stationery project is linked to Business Card Project:
http://gigs.brieftable.example/task.aspx?id=517264
Updates

Project Deadline Extended
Reason: I would like to see the business card & letterhead coordinated.

Target Market(s)

Professional renters and white color families in a suburban area of the midwest

Industry/Entity Type

Business

Colors
fece3e
fbee3f
add136
34b8a4
34a7d8
3176b5
faa54b

Requirements
Must have
• logo at top, simple not fussy font
Should not have
• shading and graduated hard to copy color

```html
<!DOCTYPE html>
<html lang="en">
<head>
<meta charset="utf-8">
<title>Larkvale Residences Stationery</title>
<link rel="stylesheet" href="https://fonts.googleapis.com/css2?family=Arimo:wght@400;700&display=swap">
<style>
  :root {
    --backdrop: #e8e5e1;
    --paper: #ffffff;
    --lime: #add136;
    --navy: #2f5a8c;
    --ocean: #3176b5;
    --sky: #34a7d8;
    --sun: #faa54b;
    --ink: #2a2a2a;
    --text: #222222;
  }
  * { margin: 0; padding: 0; box-sizing: border-box; }
  html, body { width: 1200px; height: 899px; overflow: hidden; }
  body {
    position: relative;
    background: var(--backdrop);
    font-family: "Arimo", Arial, sans-serif;
    color: var(--text);
  }
  .sheet {
    position: absolute;
    background: var(--paper);
    box-shadow: 0 1px 4px rgba(0,0,0,.18);
    overflow: hidden;
  }
  .brand {
    display: flex;
    align-items: center;
    gap: 7px;
    color: var(--ink);
    font-weight: 700;
    white-space: nowrap;
  }
  .brand-dot {
    border-radius: 50%;
    background: var(--sun);
    flex: none;
  }

  /* Letterhead */
  .letterhead { left: 15px; top: 20px; width: 550px; height: 869px; }
  .letterhead .brand { position: absolute; left: 40px; top: 50px; font-size: 17px; }
  .letterhead .brand-dot { width: 14px; height: 14px; }
  .letterhead-footer { position: absolute; left: 0; bottom: 0; width: 550px; height: 75px; }
  .letterhead-footer svg { position: absolute; inset: 0; }
  .footer-info {
    position: absolute;
    top: 23px;
    color: #fff;
    font-size: 11.5px;
    line-height: 13px;
  }
  .footer-info.mail { left: 108px; }
  .footer-info.phone { left: 253px; }
  .footer-info.place { left: 369px; }
  .footer-marker {
    position: absolute;
    top: 24px;
    width: 7px;
    height: 20px;
    background: var(--lime);
  }

  /* Envelope back */
  .envelope-back { left: 582px; top: 31px; width: 590px; height: 287px; }
  .envelope-flap {
    position: absolute;
    left: 0; top: 0;
    width: 590px; height: 76px;
    background: var(--lime);
    border-radius: 0 0 26px 26px;
  }

  /* Envelope front */
  .envelope-front { left: 582px; top: 357px; width: 590px; height: 288px; }
  .envelope-front svg { position: absolute; inset: 0; }
  .envelope-front .brand {
    position: absolute;
    left: 0; right: 0; top: 115px;
    justify-content: center;
    font-size: 24px;
  }
  .envelope-front .brand-dot { width: 20px; height: 20px; }
  .envelope-contact {
    position: absolute;
    left: 0; right: 0; top: 226px;
    text-align: center;
    font-size: 12px;
    line-height: 15px;
  }
  .envelope-contact .label { font-size: 10px; }
  .envelope-contact .web { letter-spacing: 6px; font-size: 11px; }
</style>
</head>
<body>

<section class="sheet letterhead">
  <div class="brand"><span class="brand-dot"></span>Larkvale Residences</div>
  <footer class="letterhead-footer">
    <svg width="550" height="75" viewBox="0 0 550 75">
      <defs>
        <linearGradient id="footerBand" x1="0" x2="1" y1="0" y2="0">
          <stop offset="0" stop-color="var(--navy)"/>
          <stop offset="0.45" stop-color="var(--sky)"/>
          <stop offset="1" stop-color="var(--navy)"/>
        </linearGradient>
      </defs>
      <path d="M0 6 Q275 -12 550 14 L550 75 L0 75 Z" fill="url(#footerBand)"/>
      <rect x="0" y="52" width="550" height="5" fill="var(--lime)"/>
    </svg>
    <div class="footer-info mail">hello@larkvale.example<br>www.larkvale.example</div>
    <span class="footer-marker" style="left:238px"></span>
    <div class="footer-info phone">+2348015550142<br>+2348015550142</div>
    <span class="footer-marker" style="left:356px"></span>
    <div class="footer-info place">42c fern lane,<br>Dayton</div>
  </footer>
</section>

<section class="sheet envelope-back">
  <div class="envelope-flap"></div>
</section>

<section class="sheet envelope-front">
  <svg width="590" height="288" viewBox="0 0 590 288">
    <line x1="-10" y1="140" x2="170" y2="-10" stroke="var(--lime)" stroke-width="10"/>
    <line x1="-10" y1="167" x2="186" y2="-6" stroke="var(--navy)" stroke-width="10"/>
    <line x1="-10" y1="176" x2="196" y2="-6" stroke="var(--sky)" stroke-width="6"/>
    <line x1="-10" y1="194" x2="216" y2="-6" stroke="var(--lime)" stroke-width="10"/>
    <line x1="480" y1="294" x2="600" y2="186" stroke="var(--lime)" stroke-width="10"/>
  </svg>
  <div class="brand"><span class="brand-dot"></span>Larkvale Residences</div>
  <div class="envelope-contact">
    <div class="label">Contact Address:</div>
    <div>42c fern lane, Dayton</div>
    <div>+2348015550142</div>
    <div class="web">www.larkvale.example</div>
  </div>
</section>

</body>
</html>
```